Small Firewood bag design (for use it retail stores NZ)

Hi, we are a small business in New Zealand selling firewood. We have started to bag our wood and are now selling to stores in NZ. We are in need of a good firewood bag design. The overall size to be 40cm high x 25cm wide, however the text should be at minimum 2cm within this, as to prevent it from going around the corner of the bag.
We will only be printing the label on 1 side of the bag, and would like a design for black printing only and a design with black and orange/flame color.
Our business is called 'Ember Crest Firewood', (ECF Limited)
The product/wood type is Black Wattle.
The wood is a very hardwood, makes a great burner, burns hot and long, especially when compared to pine.
Our firewood is naturally seasoned outside in the northland sun.
Black wattle is of the Acacia family from Australia.
The bags are only small, 12kg or 25 litres.
It will be printed onto clear woven PP bags, see image. So intricate drawings is not recommended.
There will be no barcode on the label, as this will be sewn onto the bag separately.
Can provide our contact details for the bag later.

Note, the below images I designed on an online AI program, but do quite like the look of them.

Target Market(s)

Will be for sale in large department stores, petrol stations, some liquor stores and some dairy's. Target market is older people, people going to the batch, wood for people not organized to get in bulk amounts of wood

Industry/Entity Type

Firewood, home heating, winter, cold

Colors

Designer to choose colors to be used in the design.

Requirements
Nice to have
• Possibly an image of logs with the flames around it

```html
<!DOCTYPE html>
<html lang="en">
<head>
<meta charset="utf-8">
<title>Ember Crest Firewood – Bag Label</title>
<link rel="stylesheet" href="https://fonts.googleapis.com/css2?family=Archivo:wght@400;600;800;900&family=Roboto+Condensed:wght@400&display=swap">
<style>
  :root {
    --bg: #000000;
    --flame: #f58220;
    --ink: #000000;
    --soft-text: #c9c9c9;
    --rule: #5a5a5a;
  }
  * { margin: 0; padding: 0; box-sizing: border-box; }
  html, body { width: 1200px; height: 750px; overflow: hidden; background: var(--bg); }
  .label {
    position: relative;
    width: 1200px;
    height: 750px;
    background: var(--bg);
    font-family: "Archivo", Arial, sans-serif;
    color: var(--flame);
  }
  .brand-name {
    position: absolute;
    left: 259px;
    top: 56px;
    width: 680px;
    font-family: "Archivo", Arial, sans-serif;
    font-weight: 900;
    font-size: 104px;
    line-height: 116px;
    letter-spacing: -2px;
    color: var(--flame);
    text-align: left;
    text-transform: uppercase;
  }
  .log-art {
    position: absolute;
    left: 254px;
    top: 301px;
    width: 692px;
    height: 137px;
  }
  .log-title {
    position: absolute;
    left: 337px;
    top: 342px;
    font-weight: 800;
    font-size: 43px;
    line-height: 44px;
    color: var(--ink);
    letter-spacing: -0.3px;
  }
  .log-caption {
    position: absolute;
    left: 342px;
    top: 388px;
    font-family: "Roboto Condensed", "Arial Narrow", sans-serif;
    font-size: 15px;
    color: var(--ink);
  }
  .story {
    position: absolute;
    left: 0;
    top: 434px;
    width: 1188px;
    text-align: center;
    font-family: "Roboto Condensed", "Arial Narrow", sans-serif;
    font-size: 17px;
    line-height: 21px;
    color: var(--soft-text);
  }
  .usage-box {
    position: absolute;
    left: 272px;
    top: 489px;
    width: 656px;
    height: 68px;
    border: 2px solid var(--flame);
  }
  .usage-box .uses {
    height: 34px;
    border-bottom: 2px solid var(--flame);
    font-weight: 600;
    font-size: 22px;
    line-height: 33px;
    text-align: center;
    white-space: nowrap;
  }
  .usage-box .outlets {
    font-size: 16.5px;
    line-height: 30px;
    text-align: center;
    white-space: nowrap;
  }
  .promise {
    position: absolute;
    left: 0;
    top: 583px;
    width: 1198px;
    text-align: center;
    font-size: 28px;
    line-height: 34px;
  }
  .divider {
    position: absolute;
    left: 65px;
    top: 659px;
    width: 1070px;
    height: 1px;
    background: var(--rule);
  }
  .features {
    position: absolute;
    left: 63px;
    top: 681px;
    width: 1075px;
    font-size: 20.5px;
    white-space: nowrap;
    text-align: center;
  }
</style>
</head>
<body>
  <main class="label">
    <h1 class="brand-name">Ember Crest<br>Firewood</h1>

    <svg class="log-art" viewBox="0 0 692 137" role="img" aria-label="Illustration of a split hardwood log with growth rings on its cut end">
      <rect x="0" y="6" width="692" height="125" rx="62" fill="#f58220"/>
    </svg>
    <p class="log-title">SEASONED HARDWOOD</p>
    <p class="log-caption">THE PRODUCT/WOOD TYPE IS BLACK WATTLE. THE WOOD IS A VERY HARDWOOD,</p>

    <p class="story">makes a great burner, burns hot and long, especially when compared to pine.<br>Our firewood is naturally seasoned outside in the northland sun.</p>

    <div class="usage-box">
      <p class="uses">USE: FIREWOOD &nbsp;I&nbsp; HOME HEATING &nbsp;I&nbsp; WINTER &nbsp;I&nbsp; COLD</p>
      <p class="outlets">PETROL STATIONS I SOME LIQUOR STORES AND SOME DAIRY'S.</p>
    </div>

    <p class="promise">NATURALLY, OPEN-AIR SEASONED FOR OPTIMAL<br>BURNING AND EASE OF LIGHTING</p>

    <div class="divider"></div>

    <p class="features">FREE FROM ACCELERANTS SUSTAINABLY SOURCED LOW MOISTURE CONTENT FOR CLEANER BURNING</p>
  </main>
</body>
</html>
```